Brightwell Galley Hour Podcast

We need a Podcast Cover design that is compatible with Apple Podcasts, Spotify, etc. In this podcast, we interview the real movers & shakers in the foodservice industry who cut through the noise to get to the top.

```html
<!DOCTYPE html>
<html lang="en">
<head>
<meta charset="utf-8">
<title>Brightwell Galley Hour Podcast – Cover</title>
<link href="https://fonts.googleapis.com/css2?family=Oswald:wght@600;700&family=Montserrat:wght@600;700&display=swap" rel="stylesheet">
<style>
  :root {
    --gold: #f2bb22;
    --gold-deep: #e0a416;
    --gold-soft: #f7cf4c;
    --royal: #3552a8;
    --navy: #1c2d52;
    --skin: #c9906c;
    --shirt: #dfe6f2;
    --white: #ffffff;
  }
  html, body {
    margin: 0;
    padding: 0;
    width: 1200px;
    height: 1200px;
    overflow: hidden;
    background: var(--gold);
  }
  .cover {
    position: relative;
    width: 1200px;
    height: 1200px;
    overflow: hidden;
  }
  .cover__backdrop {
    position: absolute;
    inset: 0;
    background: linear-gradient(160deg, var(--gold-soft) 0%, var(--gold) 45%, var(--gold-deep) 100%);
  }
  .cover__host-photo {
    position: absolute;
    inset: 0;
  }
  .cover__type {
    position: absolute;
    inset: 0;
  }
  .show-title {
    font-family: "Oswald", "Arial Narrow", sans-serif;
    font-weight: 700;
    fill: var(--royal);
  }
  .show-label {
    font-family: "Montserrat", "Helvetica", sans-serif;
    font-weight: 600;
    fill: var(--white);
  }
  .host-with {
    font-family: "Montserrat", "Helvetica", sans-serif;
    font-weight: 700;
    fill: var(--royal);
  }
  .host-name {
    font-family: "Oswald", "Arial Narrow", sans-serif;
    font-weight: 600;
    fill: var(--white);
  }
</style>
</head>
<body>
  <main class="cover">
    <div class="cover__backdrop" role="img" aria-label="Restaurant dining hall photograph tinted in golden yellow"></div>

    <svg class="cover__host-photo" width="1200" height="1200" viewBox="0 0 1200 1200" xmlns="http://www.w3.org/2000/svg" role="img" aria-label="Photograph of the smiling podcast host in a navy blazer and light checked shirt">
      <defs>
        <linearGradient id="host-tones" x1="0" y1="0" x2="0" y2="1">
          <stop offset="0" stop-color="var(--skin)"/>
          <stop offset="0.5" stop-color="var(--skin)"/>
          <stop offset="0.6" stop-color="var(--shirt)"/>
          <stop offset="0.72" stop-color="var(--navy)"/>
          <stop offset="1" stop-color="var(--navy)"/>
        </linearGradient>
      </defs>
      <path d="M392 1200 L430 850 Q470 770 660 720 L770 660 Q748 560 760 420 Q790 60 990 52 Q1200 60 1200 420 L1200 1200 Z" fill="url(#host-tones)" opacity="0.92"/>
    </svg>

    <svg class="cover__type" width="1200" height="1200" viewBox="0 0 1200 1200" xmlns="http://www.w3.org/2000/svg">
      <text class="show-title" x="82" y="290" font-size="150" textLength="620" lengthAdjust="spacingAndGlyphs">BRIGHTWELL</text>
      <text class="show-title" x="82" y="460" font-size="150" textLength="620" lengthAdjust="spacingAndGlyphs">GALLEY HOUR</text>

      <text class="show-label" x="84" y="560" font-size="64" textLength="532" lengthAdjust="spacing">PODCAST</text>

      <text class="host-with" x="84" y="972" font-size="76" textLength="260" lengthAdjust="spacing">WITH</text>
      <text class="host-name" x="82" y="1116" font-size="128" textLength="672" lengthAdjust="spacingAndGlyphs">RAFE DELGADO</text>
    </svg>
  </main>
</body>
</html>
```